Fresh & Clean *NEW* BUSINESS CARD Needed - OPTOMETRY Clinic/Optical

High-tech optometry practice with 3 doctors seeking new business card.  We provide eye exams, sell, designer glasses/contacts/specialty eyewear and treat ocular diseases.  For our business cards, we are seeking fresh, clean, and crisp design as we grow our team (staffing change).  Simply adding doctors is making the card look busy/cluttered.
 Looking for professional, less cluttered look yet still have our logo, doctor names, phone, address, and website....If possible!  :)
Names:
Marcia Trelford, O.D.
Ned Pallister, O.D.
Oona Ferrant, O.D.
Phone: 555-014-2738
Website: www.BrightLensHub.example
Address:  417 Garnet R. Holloway, Maple Hollow, NV 00000
Ultimately we have the main business card with all doctor sames and that card has two versions  (front is always the same).  The back has two designs (1) displays next appointment time/date, (2) for "general use" (non-appointment.)    I have attached what we have used in the past.  
We also need a design template for each team member in our practice with their name, title, and email.   Those should be designed with the "general use" back (see attached).
**Open to entirely new design so don't feel obligated to keep current format.  Need new perspective!  Also including our watermark and some other design features we have consistently used in past in our portfolio.  Included are two options for logos--vertical and horizontal.
**I also would like to remove "Member of Sight Alliance" on our logo if possible**
 Other image files available upon request.

Target Market(s)

New patient & Current Patients

Industry/Entity Type

Optometry

Contact Information for Business Card

High-tech optometry practice with 3 doctors seeking new business card.  We provide eye exams, sell, designer glasses/contacts/specialty eyewear and treat ocular diseases.  For our business cards, we are seeking fresh, clean, and crisp design as we grow our team (staffing change).  Simply adding doctors is making the card look busy/cluttered.  Looking for professional, less cluttered look yet still have our logo, doctor names, phone, address, and website....If possible!  :) Names: Marcia Trelford, O.D. Ned Pallister, O.D. Oona Ferrant, O.D. Phone: 555-014-2738 Website: www.BrightLensHub.example Address:  417 Garnet R. Holloway, Maple Hollow, NV 00000 Ultimately we have the main business card with all doctor sames and that card has two versions  (front is always the same).  The back has two designs (1) displays next appointment time/date, (2) for "general use" (non-appointment.)    I have attached what we have used in the past.   We also need a design template for each team member in our practice with their name, title, and email.   Those should be designed with the "general use" back (see attached). **Open to entirely new design so don't feel obligated to keep current format.  Need new perspective!  Also including our watermark and some other design features we have consistently used in past in our portfolio.  Included are two options for logos--vertical and horizontal. **I also would like to remove "Member of Sight Alliance" on our logo if possible**  Other image files available upon request.

Font styles to use
Other font styles liked:
• We have used Montserrat / Yellowtail in the past

Colors

Designer to choose colors to be used in the design.

Requirements
Must have
• Clean & Fresh Design with Logo / Info provided in description. Horizontal orientation. **I have included the CMYK colors we currently have in our logo.
Should not have
• Cluttered

```html
<!DOCTYPE html>
<html lang="en">
<head>
<meta charset="utf-8">
<title>Bright Lens Hub – Business Cards</title>
<link rel="stylesheet" href="https://fonts.googleapis.com/css2?family=Arimo:wght@400;700&family=Montserrat:wght@300&display=swap">
<style>
  :root {
    --page: #d3d3d3;
    --card: #ffffff;
    --aqua: #a6dce8;
    --aqua-text: #9fd7e5;
    --slate: #5a5a5a;
    --band-grey: #9a9696;
    --ink: #333333;
    --rule: #333333;
  }
  * { margin: 0; padding: 0; box-sizing: border-box; }
  html, body { width: 857px; height: 1200px; overflow: hidden; }
  body { background: var(--page); font-family: "Arimo", Arial, sans-serif; position: relative; }

  .card { position: absolute; left: 200px; width: 465px; height: 278px; background: var(--card); border-radius: 14px; overflow: hidden; }
  .card--front { top: 109px; }
  .card--appointment { top: 439px; }
  .card--general { top: 770px; background: var(--aqua); }

  .brand { position: absolute; display: flex; align-items: center; gap: 12px; }
  .brand__dot { width: 44px; height: 44px; border-radius: 50%; background: var(--aqua); }
  .brand__name { font-family: "Montserrat", Arial, sans-serif; font-weight: 300; font-size: 28px; color: var(--slate); letter-spacing: 0.5px; white-space: nowrap; }

  .card--front .brand { left: 26px; top: 28px; }
  .doctors { position: absolute; left: 30px; top: 106px; list-style: none; font-weight: 700; font-size: 14px; line-height: 16px; color: var(--aqua-text); }
  .practice-label { position: absolute; left: 26px; top: 175px; font-size: 12px; color: var(--aqua-text); }
  .practice-rule { position: absolute; left: 26px; top: 193px; width: 401px; height: 1px; background: var(--aqua); }
  .contact { position: absolute; left: 26px; top: 200px; list-style: none; font-size: 10px; color: var(--ink); }
  .contact li { display: flex; align-items: center; gap: 9px; height: 16px; }
  .contact svg { width: 12px; height: 12px; }
  .address-band { position: absolute; left: 0; top: 241px; width: 100%; height: 25px; }
  .address-band__text { position: absolute; left: 28px; top: 248px; font-size: 10px; color: #ffffff; white-space: nowrap; }

  .card--appointment .brand { left: 96px; top: 36px; }
  .appointment-title { position: absolute; left: 0; width: 100%; top: 106px; text-align: center; font-weight: 700; font-size: 18px; color: var(--aqua-text); letter-spacing: 0.3px; }
  .slot { position: absolute; left: 33px; width: 402px; height: 14px; font-size: 10.5px; color: var(--ink); }
  .slot--first { top: 151px; }
  .slot--second { top: 193px; }
  .slot__label { position: absolute; top: 0; }
  .slot__label--date { left: 0; }
  .slot__label--time { left: 282px; }
  .slot__line { position: absolute; top: 8px; height: 1px; background: var(--rule); }
  .slot__line--date { left: 33px; width: 240px; }
  .slot__line--time { left: 315px; width: 87px; background: #666; }
  .notice { position: absolute; left: 0; width: 100%; top: 235px; text-align: center; font-size: 10.5px; line-height: 13px; color: var(--ink); letter-spacing: 0.3px; }
  .bottom-band { position: absolute; left: 0; bottom: 0; width: 100%; height: 6px; background: var(--aqua); }

  .card--general .brand { right: 40px; bottom: 42px; gap: 7px; }
  .card--general .brand__dot { width: 22px; height: 22px; background: var(--slate); }
  .card--general .brand__name { font-size: 13px; font-weight: 300; color: var(--slate); }
</style>
</head>
<body>

<section class="card card--front" aria-label="Front of business card">
  <div class="brand">
    <span class="brand__dot"></span>
    <span class="brand__name">Bright Lens Hub</span>
  </div>
  <ul class="doctors">
    <li>Marcia Trelford, O.D.</li>
    <li>Ned Pallister, O.D.</li>
    <li>Oona Ferrant, O.D.</li>
  </ul>
  <p class="practice-label">Bright Lens Hub</p>
  <div class="practice-rule"></div>
  <ul class="contact">
    <li>
      <svg viewBox="0 0 12 12" aria-hidden="true"><circle cx="6" cy="6" r="6" fill="#a6dce8"/><rect x="3.5" y="3" width="5" height="6" rx="1" fill="none" stroke="#fff" stroke-width="1"/></svg>
      555-014-2738
    </li>
    <li>
      <svg viewBox="0 0 12 12" aria-hidden="true"><circle cx="6" cy="6" r="6" fill="#a6dce8"/><circle cx="6" cy="6" r="3.2" fill="none" stroke="#fff" stroke-width="1"/><line x1="2.8" y1="6" x2="9.2" y2="6" stroke="#fff" stroke-width="0.8"/></svg>
      www.BrightLensHub.example
    </li>
  </ul>
  <svg class="address-band" viewBox="0 0 465 25" preserveAspectRatio="none" aria-hidden="true">
    <polygon points="0,0 288,0 273,25 0,25" fill="#a6dce8"/>
    <polygon points="294,0 465,0 465,25 279,25" fill="#9a9696"/>
  </svg>
  <p class="address-band__text">417 Garnet R. Holloway, Maple Hollow, NV 00000</p>
</section>

<section class="card card--appointment" aria-label="Appointment back of business card">
  <div class="brand">
    <span class="brand__dot"></span>
    <span class="brand__name">Bright Lens Hub</span>
  </div>
  <h2 class="appointment-title">Your Next Appointetment</h2>
  <div class="slot slot--first">
    <span class="slot__label slot__label--date">Date</span>
    <span class="slot__line slot__line--date"></span>
    <span class="slot__label slot__label--time">Time</span>
    <span class="slot__line slot__line--time"></span>
  </div>
  <div class="slot slot--second">
    <span class="slot__label slot__label--date">Date</span>
    <span class="slot__line slot__line--date"></span>
    <span class="slot__label slot__label--time">Time</span>
    <span class="slot__line slot__line--time"></span>
  </div>
  <p class="notice">If your unable to keep your appoinment<br>kindly give us 24 hour notice</p>
  <div class="bottom-band"></div>
</section>

<section class="card card--general" aria-label="General use back of business card">
  <div class="brand">
    <span class="brand__dot"></span>
    <span class="brand__name">Bright Lens Hub</span>
  </div>
</section>

</body>
</html>
```